Powder Fair Flyer A5 size please

I have a very very tight timeline please, so I need a design asap. Also I need it in a 'closest to A5' size (216mm x 139mm) as specified by Printlume (not the A4 size as selected, as A5 is not available as an option) Also double sided colour.

I need a flyer which gives the feeling of snow, family and 'new season's gear on sale, ALWAYS' . The ALWAYS ON SALE is a new direction for us which means that everything is always discounted, even the latest 2014 product.

We are a family store trying to heavily promote our online presence and new pricing by putting these postcards in the bags of people visiting the powder fair in Sydney and Melbourne.

I would like the flyer to have blue colour with a snowy feel but with red starbursts similar to the products on our website. A similar look and feel to our website would be ideal

www.frostpeakgear.com.au

FRONT

Most prominent part:                   FrostPeakGear.com.au

Tag line:                                             New Season’s Gear ALWAYS ON SALE

                                                            The Glacier Trail Alpine Store for you and your family

 

Other info to include:                     Free Shipping on Orders over $100 *Conditions apply

 

Our Logo, address & Phone          712 Hollowmere St, Brindlewood VIC

                                                            Ph. 03 9467 2518

 

 

BACK

Header:                                              New Season’s Gear ALWAYS ON SALE

                                                            …why pay more?

 

Footer:                                               Plus all our regular infamous services for those who want to visit us in store:

·        Specialist boot fitting & custom Footbeds

·        Junior Kit Trade-In Scheme

·        Sell your pre-loved gear instore and online

·        Clothing, Apres and Toboggan Hire

·        Equipment Servicing

·        More stock in store than listed online

 

Center main content within starbusts (similarly to our website discounting)

·        Minimum 10% off all 2014 Gear ALWAYS *Excluding ski boots & Vidzo

·        15% off Kelt outerwear ALWAYS

·        30% off Thermex thermals ALWAYS

·        20%  off Vanta Helmet and Goggle combos ALWAYS

·        20% off Harlo Helmet and Goggle combos ALWAYS

·        Buy 2 or more Pine Hollow Merino socks for $20 ea. ALWAYS

Target Market(s)

Families who want to buy on sale

Industry/Entity Type

Store

Requirements
Must have
• Red Starbusts
Snowy feel

```html
<!DOCTYPE html>
<html lang="en">
<head>
<meta charset="utf-8">
<title>FrostPeakGear – Powder Fair Flyer</title>
<link rel="stylesheet" href="https://fonts.googleapis.com/css2?family=Lato:ital,wght@0,300;0,400;0,700;0,900;1,300&display=swap">
<style>
  :root{
    --page:#ffffff;
    --front-blue:#1f67c4;
    --front-blue-light:#3a8ee0;
    --back-navy:#17346f;
    --back-blue:#1f6fc6;
    --sky:#4fb2ee;
    --white:#ffffff;
    --burst-red:#e4202b;
    --brand-ink:#2a4f8e;
    --brand-tile:#4a9be0;
  }
  *{margin:0;padding:0;box-sizing:border-box}
  html,body{width:1200px;height:1000px;overflow:hidden;background:var(--page)}
  body{position:relative;font-family:"Lato",Arial,sans-serif;color:var(--white)}
  .sheet{position:absolute;top:76px;width:549px;height:846px;overflow:hidden}
  .sheet--front{left:38px;background:radial-gradient(ellipse at 60% 40%,var(--front-blue-light) 0%,var(--front-blue) 60%,#1b5bb3 100%)}
  .sheet--back{left:614px;background:linear-gradient(180deg,var(--back-navy) 0%,#1d4f9c 45%,var(--back-blue) 100%)}
  .abs{position:absolute;white-space:nowrap}

  .site-url{left:24px;top:58px;font-size:41px;font-weight:700;color:var(--sky);letter-spacing:-1px}
  .ribbon{right:-58px;top:38px;width:250px;height:30px;background:var(--burst-red);transform:rotate(45deg);
    text-align:center;font-size:15px;font-weight:900;line-height:30px;letter-spacing:1px}
  .front-kicker{left:24px;top:122px;font-size:55px;font-weight:900;letter-spacing:-3px;line-height:1}
  .front-headline{left:20px;top:176px;font-size:128px;font-weight:900;letter-spacing:-7px;line-height:107px;
    text-shadow:0 4px 8px rgba(0,0,0,.25)}
  .front-tag{left:0;width:100%;top:408px;text-align:center;font-size:29px;font-weight:900;letter-spacing:-1.5px;line-height:1}

  .burst{position:absolute}
  .burst svg.shape{position:absolute;inset:0;width:100%;height:100%}
  .product{position:absolute;left:30%;top:30%;width:40%;height:40%}

  .address{right:27px;top:740px;font-size:22px;font-weight:900;letter-spacing:-1px}
  .phone{left:182px;top:772px;display:flex;align-items:center;gap:18px}
  .phone-icon{width:36px;height:36px}
  .phone-number{font-size:50px;font-weight:900;letter-spacing:-3px;line-height:1}

  .back-kicker{left:42px;top:43px;font-size:27px;font-weight:900;letter-spacing:-1.5px;color:var(--sky)}
  .back-headline{left:40px;top:74px;font-size:64px;font-weight:900;letter-spacing:-4px;line-height:.84}
  .back-tagline{left:44px;top:176px;font-size:30px;font-weight:300;font-style:italic;color:var(--sky)}
  .deal .deal-text{position:absolute;inset:0;display:flex;align-items:center;justify-content:center;text-align:center;
    font-size:13px;line-height:1.2;padding:0 18%}
  .deal b{font-weight:900}
  .deal--main .deal-text{font-size:18px;line-height:1.25}
  .services{left:36px;top:470px;width:360px}
  .services-lead{font-size:14.5px;font-weight:700;line-height:1.2;margin-bottom:18px}
  .services-list{list-style:none;font-size:16px;line-height:20px}
  .services-list li::before{content:"•";margin-right:2px}
  .fineprint{left:445px;top:600px;font-size:12px;transform:rotate(-90deg);transform-origin:center;width:170px;text-align:center}
  .ridge{left:0;bottom:0;width:100%;height:220px}
  .footer-ship{left:18px;top:794px;font-size:25px;font-weight:900;letter-spacing:-1.5px;color:var(--sky)}
  .footer-url{left:238px;top:800px;font-size:18px;font-weight:900;letter-spacing:-.5px;color:var(--sky)}
  .brand{left:428px;top:780px;display:flex;align-items:center;gap:6px}
  .brand-name{font-size:10px;font-weight:400;color:var(--brand-ink);line-height:1.15}
  .brand-square{width:30px;height:30px;background:var(--brand-tile)}
</style>
</head>
<body>
<svg width="0" height="0" style="position:absolute" aria-hidden="true">
  <defs>
    <symbol id="starburst" viewBox="-50 -50 100 100">
      <polygon points="50,0 39.2,7.8 46.2,19.1 33.3,22.2 35.4,35.4 22.2,33.3 19.1,46.2 7.8,39.2 0,50 -7.8,39.2 -19.1,46.2 -22.2,33.3 -35.4,35.4 -33.3,22.2 -46.2,19.1 -39.2,7.8 -50,0 -39.2,-7.8 -46.2,-19.1 -33.3,-22.2 -35.4,-35.4 -22.2,-33.3 -19.1,-46.2 -7.8,-39.2 0,-50 7.8,-39.2 19.1,-46.2 22.2,-33.3 35.4,-35.4 33.3,-22.2 46.2,-19.1 39.2,-7.8"/>
    </symbol>
    <linearGradient id="productTone" x1="0" y1="0" x2="0" y2="1">
      <stop offset="0" stop-color="#8fa6c2"/><stop offset="1" stop-color="#4b5f7a"/>
    </linearGradient>
    <linearGradient id="snowRidge" x1="0" y1="0" x2="0" y2="1">
      <stop offset="0" stop-color="#ffffff" stop-opacity="0"/>
      <stop offset=".55" stop-color="#dfeaf6" stop-opacity=".7"/>
      <stop offset="1" stop-color="#ffffff"/>
    </linearGradient>
  </defs>
</svg>

<section class="sheet sheet--front" aria-label="Flyer front">
  <div class="abs ribbon">FREE SHIPPING *</div>
  <div class="abs site-url">frostpeakgear.com.au</div>
  <div class="abs front-kicker">New Season’s Gear</div>
  <div class="abs front-headline">ALWAYS<br>ON SALE</div>
  <div class="abs front-tag">The Glacier Trail Alpine Store<br>for you and your family</div>

  <div class="burst" style="left:52px;top:494px;width:104px;height:104px">
    <svg class="shape" fill="#fff"><use href="#starburst"/></svg>
    <svg class="product" role="img" aria-label="Photo of a ski helmet"><rect width="100%" height="100%" rx="12" fill="url(#productTone)"/></svg>
  </div>
  <div class="burst" style="left:137px;top:546px;width:130px;height:140px">
    <svg class="shape" fill="#fff"><use href="#starburst"/></svg>
    <svg class="product" role="img" aria-label="Photo of blue ski pants"><rect width="100%" height="100%" rx="6" fill="#2a6fc9"/></svg>
  </div>
  <div class="burst" style="left:278px;top:488px;width:128px;height:128px">
    <svg class="shape" fill="#fff"><use href="#starburst"/></svg>
    <svg class="product" role="img" aria-label="Photo of a magenta ski jacket"><rect width="100%" height="100%" rx="8" fill="#b0306f"/></svg>
  </div>
  <div class="burst" style="left:412px;top:528px;width:98px;height:98px">
    <svg class="shape" fill="#fff"><use href="#starburst"/></svg>
    <svg class="product" role="img" aria-label="Photo of ski goggles"><rect width="100%" height="100%" rx="10" fill="#5aa0c8"/></svg>
  </div>
  <div class="burst" style="left:30px;top:636px;width:108px;height:108px">
    <svg class="shape" fill="#fff"><use href="#starburst"/></svg>
    <svg class="product" role="img" aria-label="Photo of ski gloves"><rect width="100%" height="100%" rx="10" fill="#2b2d33"/></svg>
  </div>
  <div class="burst" style="left:338px;top:606px;width:120px;height:124px">
    <svg class="shape" fill="#fff"><use href="#starburst"/></svg>
    <svg class="product" role="img" aria-label="Photo of a snow boot"><rect width="100%" height="100%" rx="8" fill="#8a6a4e"/></svg>
  </div>

  <div class="abs address">712 Hollowmere St, Brindlewood VIC</div>
  <div class="abs phone">
    <svg class="phone-icon" viewBox="0 0 36 36" aria-hidden="true">
      <rect width="36" height="36" rx="6" fill="#fff"/>
      <path d="M12 8c1.5 0 3 3.5 3 5s-2 2-2 3c0 2 4 6.5 6 6.5 1 0 1.5-2 3-2s5 1.5 5 3-2 4.5-4 4.5C16 28 8 19 8 12c0-2 2.5-4 4-4z" fill="var(--front-blue)"/>
    </svg>
    <span class="phone-number">03 9467 2518</span>
  </div>
</section>

<section class="sheet sheet--back" aria-label="Flyer back">
  <div class="abs back-kicker">New Season’s Gear</div>
  <div class="abs back-headline">ALWAYS<br>ON SALE</div>
  <div class="abs back-tagline">Why pay more?</div>

  <div class="burst deal" style="left:396px;top:44px;width:108px;height:108px">
    <svg class="shape" fill="var(--burst-red)"><use href="#starburst"/></svg>
    <div class="deal-text"><span>30% off Thermex Thermals <b>ALWAYS</b></span></div>
  </div>
  <div class="burst deal" style="left:322px;top:146px;width:124px;height:124px">
    <svg class="shape" fill="var(--burst-red)"><use href="#starburst"/></svg>
    <div class="deal-text"><span>20% off Vanta Helmet and Goggle combos <b>ALWAYS</b></span></div>
  </div>
  <div class="burst deal" style="left:400px;top:262px;width:116px;height:116px">
    <svg class="shape" fill="var(--burst-red)"><use href="#starburst"/></svg>
    <div class="deal-text"><span>Up to 70% off selected products Store wide</span></div>
  </div>
  <div class="burst deal deal--main" style="left:174px;top:256px;width:180px;height:180px">
    <svg class="shape" fill="var(--burst-red)"><use href="#starburst"/></svg>
    <div class="deal-text"><span>Minimum 10% off all 2014 Gear <b>ALWAYS*</b></span></div>
  </div>
  <div class="burst deal" style="left:28px;top:292px;width:128px;height:128px">
    <svg class="shape" fill="var(--burst-red)"><use href="#starburst"/></svg>
    <div class="deal-text"><span>20% off Harlo Helmet and Goggle combos <b>ALWAYS</b></span></div>
  </div>
  <div class="burst deal" style="left:356px;top:412px;width:122px;height:122px">
    <svg class="shape" fill="var(--burst-red)"><use href="#starburst"/></svg>
    <div class="deal-text"><span>15% off Kelt outerwear <b>ALWAYS</b></span></div>
  </div>
  <div class="burst deal" style="left:342px;top:560px;width:148px;height:148px">
    <svg class="shape" fill="var(--burst-red)"><use href="#starburst"/></svg>
    <div class="deal-text"><span>Buy 2 or more Pine Hollow Merino socks for $20 ea. <b>ALWAYS</b></span></div>
  </div>

  <div class="abs services">
    <p class="services-lead">Plus all our regular infamous services<br>for those who want to visit us in store:</p>
    <ul class="services-list">
      <li>Specialist boot fitting &amp; custom Footbeds</li>
      <li>Junior Kit Trade-In Scheme</li>
      <li>Sell your pre-loved gear instore and online</li>
      <li>Clothing, Apres and Toboggan Hire</li>
      <li>Equipment Servicing</li>
      <li>More stock in store than listed online</li>
    </ul>
  </div>
  <div class="abs fineprint">* Excluding ski boots &amp; Vidzo</div>

  <svg class="abs ridge" role="img" aria-label="Snowy mountain ridge illustration" preserveAspectRatio="none" viewBox="0 0 549 220">
    <rect width="549" height="220" fill="url(#snowRidge)"/>
  </svg>

  <div class="abs footer-ship">FREE SHIPPING</div>
  <div class="abs footer-url">frostpeakgear.com.au</div>
  <div class="abs brand">
    <span class="brand-name">frost peak<br>brindlewood</span>
    <span class="brand-square"></span>
  </div>
</section>
</body>
</html>
```